QuillaVorn needs a dashboard page designed

Redesign the dashboard shown in the provided images.

There are two images:
- dashboard.png
- dashboard-expanded.png

NOTE: The vocabulary navigation on the left will be a very long list of words 100s, so keep that in mind when you're designing both the vocab navigation and the expanded vocab popup.

In the dashboard.png picture, there needs to be a progress chart showing the word progress like the following: review 1(show it as completed) -> review 2(show the user they are here) -> review 3(unvisited) -> review 4(unvisited)

The do-not-design-this-page.png image is for your reference only. It is not to be designed. Use it to understand the overall look and feel of the website to help you create the best dashboard page possible.
Updates

Need extra days to review

Industry/Entity Type

Education English learning

Number of Pages Required

1 page

Requirements
Must have
• The main navigation and main header cannot change between pages. See the do-not-design page for the main navigateion and header.
Should not have
• Do not add a person profile. We will not have images of our users. Keep the icons in the main navigation as they are.

```html
<!DOCTYPE html>
<html lang="en">
<head>
<meta charset="utf-8">
<title>Lexi Mentor – Dashboard</title>
<link rel="stylesheet" href="https://fonts.googleapis.com/css2?family=Nunito+Sans:wght@400;600;700;800&family=Roboto:wght@400;500&display=swap">
<style>
:root{
  --page:#f7f7f8;
  --card:#ffffff;
  --ink:#2a2f36;
  --panel:#2e353e;
  --panel-text:#aab1ba;
  --panel-head:#e9ecef;
  --accent:#4a86c5;
  --bar:#2c62b0;
  --muted:#9aa0a6;
  --line:#d9dde2;
  --band-long:#e9eff7;
  --band-work:#edf5ec;
  --band-short:#fdfbea;
  --band-lost:#f2f2f2;
  --star:#f5b82e;
}
*{box-sizing:border-box;margin:0;padding:0}
html,body{width:1200px;height:819px;overflow:hidden;background:var(--page);font-family:"Nunito Sans",sans-serif;color:var(--ink)}
.card{position:absolute;left:61px;top:61px;width:1078px;height:697px;background:var(--card);border-radius:26px;box-shadow:0 6px 30px rgba(0,0,0,.05);overflow:hidden}
.topbar-menu{position:absolute;left:30px;top:25px}
.topbar-title{position:absolute;left:0;width:1078px;top:25px;text-align:center;font-size:9px;font-weight:600}
.topbar-title svg{vertical-align:middle;margin-left:3px}
.topbar-icons{position:absolute;right:32px;top:23px;display:flex;gap:10px;align-items:center}
.main-nav{position:absolute;left:13px;top:102px;width:116px}
.nav-item{display:flex;align-items:center;gap:9px;height:37px;padding-left:18px;font-size:8.6px;font-weight:700;margin-bottom:3px}
.nav-item.active{background:var(--panel);color:#fff;border-radius:19px 0 0 19px}
.workspace{position:absolute;left:129px;top:62px;width:949px;height:635px;background:var(--panel);border-radius:30px 30px 0 30px}
.vocab{position:absolute;left:0;top:0;width:145px;height:635px}
.filter{position:absolute;left:13px;top:77px;display:flex;gap:7px}
.filter-select{width:78px;height:27px;border-radius:14px;background:#3b434d;color:#e6e9ec;display:flex;align-items:center;padding:0 11px;gap:6px;font-size:8.5px;font-weight:600}
.filter-select .caret{margin-left:auto}
.filter-export{width:34px;height:27px;border-radius:14px;background:#3b434d;display:flex;align-items:center;justify-content:center}
.stage-tab{position:absolute;left:13px;top:126px;width:132px;height:36px;background:var(--card);border-radius:18px 0 0 18px;display:flex;align-items:center;gap:6px;padding-left:15px;font-size:8.6px;font-weight:700}
.word-list{position:absolute;left:38px;top:0;list-style:none;font-size:8.6px}
.word-list li{position:absolute;white-space:nowrap;color:var(--panel-text);font-weight:600;letter-spacing:.2px;line-height:11px}
.word-list li.current{color:var(--accent)}
.word-list li.stage{color:var(--panel-head);font-weight:700}
.content{position:absolute;left:145px;top:40px;width:804px;height:595px;background:var(--card);border-radius:30px 30px 0 0}
.word-title{position:absolute;top:48px;left:0;width:804px;text-align:center;font-size:14px;line-height:20px;font-weight:800}
.word-title svg{vertical-align:-2px;margin-left:3px}
.steps{position:absolute;left:159px;top:97px;display:flex;align-items:center}
.step{width:98px;height:28px;border-radius:14px;border:1px solid var(--line);display:flex;align-items:center;justify-content:center;gap:6px;font-size:8.8px;font-weight:600;color:var(--muted)}
.step.done{border-color:var(--accent);color:var(--accent)}
.step.current{background:var(--panel);border-color:var(--panel);color:#fff}
.step-link{width:31px;height:1px;background:var(--line)}
.definition{position:absolute;left:32px;top:155px;width:712px;font-size:8.8px;line-height:12.2px}
.chart-title{position:absolute;top:240px;left:0;width:804px;text-align:center;font-size:9.4px;line-height:14px;font-weight:700;padding-left:12px}
.chart{position:absolute;left:32px;top:270px;font-family:"Roboto",sans-serif}
.analysis-title{position:absolute;left:32px;top:474px;font-size:9.4px;line-height:14px;font-weight:800}
.analysis-text{position:absolute;left:32px;top:495px;width:742px;font-size:8.8px;line-height:11.8px;white-space:nowrap;overflow:hidden}
</style>
</head>
<body>
<main class="card">
  <header>
    <svg class="topbar-menu" width="24" height="15" viewBox="0 0 24 15" aria-label="Menu"><g stroke="#2a2f36" stroke-width="1.6" stroke-linecap="round"><line x1="1" y1="1.5" x2="23" y2="1.5"/><line x1="1" y1="7.5" x2="21" y2="7.5"/><line x1="1" y1="13.5" x2="16" y2="13.5"/></g></svg>
    <div class="topbar-title">Lexi Mentor<svg width="8" height="6" viewBox="0 0 8 6"><path d="M1 1.5l3 3 3-3" fill="none" stroke="#2a2f36" stroke-width="1.2"/></svg></div>
    <div class="topbar-icons">
      <svg width="14" height="14" viewBox="0 0 24 24" aria-label="Settings"><path fill="#2a2f36" d="M19.4 13a7.5 7.5 0 000-2l2.1-1.6-2-3.5-2.5 1a7.7 7.7 0 00-1.7-1L15 3h-4l-.4 2.9a7.7 7.7 0 00-1.7 1l-2.5-1-2 3.5L6.6 11a7.5 7.5 0 000 2l-2.1 1.6 2 3.5 2.5-1a7.7 7.7 0 001.7 1L11 21h4l.4-2.9a7.7 7.7 0 001.7-1l2.5 1 2-3.5zM13 15.5a3.5 3.5 0 110-7 3.5 3.5 0 010 7z"/></svg>
      <svg width="15" height="14" viewBox="0 0 24 22" aria-label="Tasks"><path d="M18 11v7a2 2 0 01-2 2H4a2 2 0 01-2-2V6a2 2 0 012-2h9" fill="none" stroke="#2a2f36" stroke-width="2.6"/><path d="M6 10l4 4 12-12" fill="none" stroke="#2a2f36" stroke-width="3"/></svg>
      <span style="display:flex;align-items:center;gap:2px"><svg width="14" height="14" viewBox="0 0 24 24" aria-label="Account"><circle cx="12" cy="12" r="10" fill="none" stroke="#2a2f36" stroke-width="2"/><circle cx="12" cy="10" r="3.5" fill="#2a2f36"/><path d="M5.5 18.5c2-3 11-3 13 0" fill="#2a2f36"/></svg><svg width="8" height="6" viewBox="0 0 8 6"><path d="M1 1.5l3 3 3-3" fill="none" stroke="#2a2f36" stroke-width="1.2"/></svg></span>
    </div>
  </header>

  <nav class="main-nav">
    <div class="nav-item active"><svg width="12" height="12" viewBox="0 0 24 24"><path fill="#fff" d="M12 2L1 12h3v10h6v-6h4v6h6V12h3z"/></svg>Lexi Mentor</div>
    <div class="nav-item"><svg width="12" height="12" viewBox="0 0 24 24"><path fill="#2a2f36" d="M12 1.5l3.2 6.8 7.3.9-5.4 5 1.4 7.3L12 17.9l-6.5 3.6 1.4-7.3-5.4-5 7.3-.9z"/></svg>Daily English</div>
    <div class="nav-item"><svg width="12" height="12" viewBox="0 0 24 24"><path fill="#2a2f36" d="M5 1h14v22h-5v-4h-4v4H5zm3 3v2h2V4zm4 0v2h2V4zm4 0v2h1V4zM8 8v2h2V8zm4 0v2h2V8zm4 0v2h1V8zM8 12v2h2v-2zm4 0v2h2v-2zm4 0v2h1v-2zM8 16v2h2v-2zm6 0v2h2v-2z"/></svg>Business</div>
  </nav>

  <section class="workspace">
    <aside class="vocab">
      <div class="filter">
        <div class="filter-select"><svg width="12" height="12" viewBox="0 0 24 24"><path fill="#c9ced4" d="M12 2l10 5-10 5L2 7zm-10 9l10 5 10-5v3l-10 5-10-5z"/></svg>All<svg class="caret" width="8" height="6" viewBox="0 0 8 6"><path d="M1 1.5l3 3 3-3" fill="none" stroke="#c9ced4" stroke-width="1.2"/></svg></div>
        <div class="filter-export"><svg width="11" height="11" viewBox="0 0 24 24"><path d="M10 3H3v18h18v-7M14 3h7v7M21 3L11 13" fill="none" stroke="#c9ced4" stroke-width="2.6"/></svg></div>
      </div>
      <div class="stage-tab"><svg width="8" height="8" viewBox="0 0 10 10"><path d="M1.5 8.5l7-7M3 1.5h5.5V7" fill="none" stroke="#2a2f36" stroke-width="1.4"/></svg>Short Term Memory</div>
      <ul class="word-list">
        <li class="current" style="top:176px">Grab</li>
        <li class="stage" style="top:219px">Working Memory</li>
        <li style="top:256px">Cool Down</li>
        <li style="top:280px">Crave</li>
        <li style="top:305px">Go For</li>
        <li style="top:329px">Go-To</li>
        <li style="top:354px">In The Mood For</li>
        <li style="top:378px">Sip</li>
        <li style="top:403px">Soothing</li>
        <li style="top:428px">Stick With</li>
        <li style="top:452px">Throw In/Throw On</li>
        <li class="stage" style="top:495px">Long-Term Memory</li>
        <li style="top:532px">Give It A Try</li>
      </ul>
    </aside>

    <article class="content">
      <h1 class="word-title">Grab<svg width="15" height="15" viewBox="0 0 24 24"><path fill="var(--star)" d="M12 1.5l3.2 6.8 7.3.9-5.4 5 1.4 7.3L12 17.9l-6.5 3.6 1.4-7.3-5.4-5 7.3-.9z"/></svg></h1>

      <div class="steps">
        <div class="step done"><svg width="12" height="12" viewBox="0 0 12 12"><circle cx="6" cy="6" r="6" fill="var(--accent)"/><path d="M3.3 6.2l1.8 1.8 3.6-3.6" fill="none" stroke="#fff" stroke-width="1.3"/></svg>Review 1</div>
        <div class="step-link"></div>
        <div class="step current"><svg width="12" height="12" viewBox="0 0 12 12"><circle cx="6" cy="6" r="6" fill="#fff"/><path d="M3.3 6.2l1.8 1.8 3.6-3.6" fill="none" stroke="var(--panel)" stroke-width="1.3"/></svg>Review 2</div>
        <div class="step-link"></div>
        <div class="step"><svg width="12" height="12" viewBox="0 0 12 12"><circle cx="6" cy="6" r="6" fill="#a4a9ae"/><path d="M3.3 6.2l1.8 1.8 3.6-3.6" fill="none" stroke="#fff" stroke-width="1.3"/></svg>Review 3</div>
        <div class="step-link"></div>
        <div class="step"><svg width="12" height="12" viewBox="0 0 12 12"><circle cx="6" cy="6" r="6" fill="#a4a9ae"/><path d="M3.3 6.2l1.8 1.8 3.6-3.6" fill="none" stroke="#fff" stroke-width="1.3"/></svg>Review 4</div>
      </div>

      <p class="definition">The word "<b>grab</b>" is the most commonly used as a <b>verb</b>, meaning <b>to take something quickly or suddenly</b>. Imagine you're running late for school. You don't have time for breakfast, so you quickly <b>grab</b> an apple from the kitchen and rush out the door. As you reach the bus stop, your friend waves and says. "Hey, let's <b>grab</b> a coffee after class". Later, when you sit down, your phone starts ringing. You <b>grab</b> it from your bag and answer.</p>

      <h2 class="chart-title">Learning Curve Graph</h2>
      <svg class="chart" width="745" height="155" viewBox="0 0 745 155" role="img" aria-label="Learning curve bar chart">
        <rect x="0" y="0" width="733" height="32" fill="var(--band-long)"/>
        <rect x="0" y="32" width="733" height="64" fill="var(--band-work)"/>
        <rect x="0" y="96" width="733" height="16" fill="var(--band-short)"/>
        <rect x="0" y="112" width="733" height="17" fill="var(--band-lost)"/>
        <g font-size="6" fill="#666">
          <text x="8" y="15">Long-Term Memory</text>
          <text x="8" y="63">Working Memory</text>
          <text x="8" y="106">Short-Term Memory</text>
          <text x="8" y="122">Forgotten Memory</text>
        </g>
        <rect x="67" y="101" width="13" height="28" fill="var(--bar)"/>
        <rect x="139" y="32" width="14" height="97" fill="var(--bar)"/>
        <path d="M84 97 C100 100,115 108,139 127" fill="none" stroke="#555" stroke-width="1" stroke-dasharray="1 3"/>
        <path d="M153 33 C200 38,220 40,233 50 C250 62,275 95,292 127" fill="none" stroke="#555" stroke-width="1" stroke-dasharray="1 3"/>
        <g>
          <rect x="46" y="88" width="36" height="13" rx="2" fill="#fff" stroke="#ddd"/>
          <text x="64" y="97" font-size="5.8" text-anchor="middle" fill="#222">May 18</text>
          <rect x="111" y="23" width="36" height="13" rx="2" fill="#fff" stroke="#ddd"/>
          <text x="129" y="32" font-size="5.8" text-anchor="middle" fill="#222">May 19</text>
        </g>
        <line x1="0" y1="129" x2="740" y2="129" stroke="#333" stroke-width="0.8"/>
        <g stroke="#333" stroke-width="0.7">
          <line x1="9" y1="129" x2="9" y2="134"/><line x1="45" y1="129" x2="45" y2="134"/><line x1="82" y1="129" x2="82" y2="134"/><line x1="118" y1="129" x2="118" y2="134"/><line x1="155" y1="129" x2="155" y2="134"/><line x1="191" y1="129" x2="191" y2="134"/><line x1="228" y1="129" x2="228" y2="134"/><line x1="264" y1="129" x2="264" y2="134"/><line x1="301" y1="129" x2="301" y2="134"/><line x1="337" y1="129" x2="337" y2="134"/><line x1="374" y1="129" x2="374" y2="134"/><line x1="410" y1="129" x2="410" y2="134"/><line x1="447" y1="129" x2="447" y2="134"/><line x1="483" y1="129" x2="483" y2="134"/><line x1="520" y1="129" x2="520" y2="134"/><line x1="556" y1="129" x2="556" y2="134"/><line x1="593" y1="129" x2="593" y2="134"/><line x1="629" y1="129" x2="629" y2="134"/><line x1="666" y1="129" x2="666" y2="134"/><line x1="702" y1="129" x2="702" y2="134"/><line x1="739" y1="129" x2="739" y2="134"/>
        </g>
        <g font-size="6" fill="#222" text-anchor="middle">
          <text x="11" y="143">18 May</text><text x="45" y="143">12:00</text><text x="82" y="143">19 May</text><text x="118" y="143">12:00</text><text x="155" y="143">20 May</text><text x="191" y="143">12:00</text><text x="228" y="143">21 May</text><text x="264" y="143">12:00</text><text x="301" y="143">22 May</text><text x="337" y="143">12:00</text><text x="374" y="143">23 May</text><text x="410" y="143">12:00</text><text x="447" y="143">24 May</text><text x="483" y="143">12:00</text><text x="520" y="143">25 May</text><text x="556" y="143">12:00</text><text x="593" y="143">26 May</text><text x="629" y="143">12:00</text><text x="666" y="143">27 May</text><text x="702" y="143">12:00</text><text x="732" y="143">28 …</text>
          <text x="370" y="153" font-weight="500">Date Range</text>
        </g>
      </svg>

      <h2 class="analysis-title">Lexi Mentor Learning Analysis</h2>
      <p class="analysis-text">Lorem ipsum dolor sit amet, consectetur adipiscing elit, sed do eiusmod tempor incididunt ut labore et dolore magna aliqua. Ut enim ad minim veniam, quis nostru<br>exercitation ullamco laboris nisi ut aliquip ex ea commodo consequat. Duis aute irure dolor in reprehenderit in voluptate velit esse cillum dolore eu fugiat nulla pari<br>atur. Excepteur sint occaecat cupidatat non proident, sunt in culpa qui officia deserunt mollit anim id est laborum.</p>
    </article>
  </section>
</main>
</body>
</html>
```